Psychotherapy Website - Based in London

I am a newly trained psychotherapist and need a new website for www.delphinecarrow.co.uk.

I offer therapy for addiction, relationships, trauma and many other issues people face in their lives.

I want the website to be welcoming, gentle, feminine and for people to feel safe.

I do not like a page site that scrolls through sections, rather each page should be separate. Here some examples that i like. Sectional rather than scrolled.

https://www.maribethvane.com/
https://www.thequietrooms.com/

The imagery should be around pink using the flower in the logo / wording and around the site:

Here is a link to the flower for ideas:
https://www.lookfindo.com/search?q=pink+gerbera

DelphineCarrow
Compassionate Psychotherapy

Is the logo and subheader for the website. Please use a typeface for the name that is appealing and professional.

Type face similar NOT EXLUSIVLY - JUST AN IDEA like this:
https://glowpostureclub.com/

Basic business card i created as a rough idea below.

I have also added the website copy.

The headers are

Homepage
About Me
Therapy
Common Questions
Blog
Contact Me

Target Market(s)

Clients who are dealing with stress, trauma, pain, addiction

Industry/Entity Type

Therapy and Psychology

Coding

Coded - Design and coding required

Number of Pages Required

5+ page

Font styles to use
Serif
Sans Serif
Script

Colors
0054AA
0677BA
7BADD7
CADEEF
E8F1F8
0094D4
00A9DD
6FCCEA
C7EBF8
E9F6FB
E54698
E96AAD
F1A4CE
F9D9EA
FCEFF6

Requirements
Must have
• Pink Gerbera Flower integrated into design
Nice to have
• Images but not to stock imagery. Needs to look authentic and natural
Should not have
• Stock images of people. Images are important but needs to feel REAL

```html
<!DOCTYPE html>
<html lang="en">
<head>
<meta charset="utf-8">
<title>Therapy – Delphine Carrow Compassionate Psychotherapy</title>
<link rel="stylesheet" href="https://fonts.googleapis.com/css2?family=Poppins:wght@400;500;600;700&display=swap">
<style>
  :root{
    --navy:#12308c;
    --pink:#d6117a;
    --pink-soft:#f9d9ea;
    --pink-pale:#fceff6;
    --ink:#1e1e1e;
    --white:#ffffff;
    --leaf-dark:#1d3a1a;
    --leaf:#3f6a2e;
    --petal:#e3338f;
  }
  *{box-sizing:border-box;margin:0;padding:0}
  html,body{width:721px;height:1200px;overflow:hidden;background:var(--white)}
  body{font-family:"Poppins",sans-serif;color:var(--ink);position:relative}

  /* Hero */
  .hero{position:absolute;left:0;top:0;width:721px;height:302px;overflow:hidden}
  .hero-photo{position:absolute;inset:0;
    background:
      radial-gradient(ellipse 420px 260px at 610px 300px,var(--petal) 0%,#e0529d 45%,rgba(224,82,157,0) 75%),
      radial-gradient(ellipse 300px 200px at 420px 290px,rgba(231,70,152,.9) 0%,rgba(231,70,152,0) 70%),
      linear-gradient(120deg,var(--leaf) 0%,var(--leaf-dark) 35%,#466f34 60%,#2c4a22 100%)}
  .hero-shade{position:absolute;inset:0;background:linear-gradient(180deg,rgba(0,0,0,.18),rgba(0,0,0,0) 40%)}
  .brand{position:absolute;left:45px;top:26px;color:var(--white)}
  .brand-name{font-weight:600;font-size:21px;line-height:26px;letter-spacing:.2px}
  .brand-tagline{font-weight:400;font-size:12.5px;letter-spacing:.6px;margin-top:8px;line-height:18px}
  .main-nav{position:absolute;top:32px;left:297px;display:flex;align-items:center;height:24px;font-size:10.4px;font-weight:500;color:var(--white)}
  .main-nav a{color:inherit;text-decoration:none;margin-right:21px}
  .main-nav a.current{color:#ff5fae}
  .main-nav a.cta{margin-right:0;margin-left:-12px;background:var(--pink);border-radius:13px;height:25px;line-height:25px;width:84px;text-align:center}
  .hero-title{position:absolute;left:0;right:0;top:138px;text-align:center;font-size:35px;font-weight:700;color:var(--white);letter-spacing:.3px}

  /* Intro */
  .intro-photo{position:absolute;left:45px;top:344px;width:308px;height:303px;
    background:linear-gradient(100deg,#d9dde2 0%,#eef0f2 35%,#c9c9c9 55%,#b89a86 75%,#2e4468 100%)}
  .intro-text{position:absolute;left:370px;top:340px;width:306px}
  .section-heading{font-size:25px;font-weight:600;color:var(--navy);line-height:32px}
  .intro-text .section-heading{margin-bottom:10px}
  .intro-text p{font-size:10.4px;line-height:17.7px;letter-spacing:.2px;margin-top:3.5px}
  .intro-wide{position:absolute;left:45px;top:658px;width:640px;font-size:10.4px;line-height:17.7px;letter-spacing:.2px}

  /* Help list */
  .help{position:absolute;left:0;top:750px;width:721px;height:326px;
    background:
      radial-gradient(ellipse 260px 180px at 150px 150px,rgba(241,164,206,.55),rgba(241,164,206,0) 70%),
      radial-gradient(ellipse 300px 220px at 600px 220px,rgba(241,164,206,.5),rgba(241,164,206,0) 70%),
      linear-gradient(180deg,#f8d6ea,#f6cde5)}
  .help .section-heading{position:absolute;left:0;right:0;top:38px;text-align:center;font-size:25.5px;font-weight:700}
  .help-list{position:absolute;top:87px;list-style:none;font-size:10.6px;letter-spacing:.2px}
  .help-list li{height:22.8px;line-height:14px;padding-left:21px;position:relative}
  .help-list li svg{position:absolute;left:0;top:3px}
  .col-a{left:45px}.col-b{left:280px}.col-c{left:497px}

  /* Footer */
  .site-footer{position:absolute;left:0;top:1076px;width:721px;height:124px;text-align:center}
  .footer-nav{margin-top:29px;font-size:10.4px;font-weight:600;display:flex;justify-content:center;gap:27px}
  .footer-nav a{color:var(--ink);text-decoration:none}
  .copyright{font-size:9.4px;margin-top:14px;color:#333}
  .social{display:flex;justify-content:center;gap:12px;margin-top:9px}
  .social span{width:12px;height:12px;border-radius:50%;background:#333;display:block}
</style>
</head>
<body>
  <header class="hero">
    <div class="hero-photo" role="img" aria-label="Close-up of a pink gerbera flower against green leaves"></div>
    <div class="hero-shade"></div>
    <div class="brand">
      <div class="brand-name">Delphine Carrow</div>
      <div class="brand-tagline">Compassionate Psychotherapy</div>
    </div>
    <nav class="main-nav">
      <a href="#">About Me</a>
      <a href="#" class="current">Therapy</a>
      <a href="#">Common Questions</a>
      <a href="#">Blog</a>
      <a href="#" class="cta">Contact Me</a>
    </nav>
    <h1 class="hero-title">Therapy</h1>
  </header>

  <main>
    <div class="intro-photo" role="img" aria-label="Therapist and client talking in a bright room with a sofa"></div>
    <section class="intro-text">
      <h2 class="section-heading">Therapy</h2>
      <p>There are times when the challenges of life can make us feel overwhelmed and isolated, and it may feel difficult to talk about how we feel to those who are closest to us.</p>
      <p>We go through transitions and crises and experience uncertainty and loss. How we deal with difficulties in life is an important aspect in how we carry on forwards and ultimately who we become as people.</p>
      <p>I offer a range of psychotherapeutic approaches includingtransactional analysis psychotherapy and relational therapy.</p>
      <p>Through the process of exploration, we enable self-knowledge and self-awareness to help you grow and conquer issues that may previously have been experienced as all-consuming or overwhelming.</p>
    </section>
    <p class="intro-wide">We will not only look at your problems in the present but also identify the roots of these problems from your past.<br>We will explore how your past experiences may have affected the way you live today and operate within your life in the present and when you become aware and understand this, it is possible for change to take place.</p>

    <section class="help">
      <h2 class="section-heading">What We Can Help With</h2>
      <ul class="help-list col-a">
        <li><svg width="10" height="8" viewBox="0 0 10 8"><path d="M1 1l3 3-3 3M5 1l3 3-3 3" fill="none" stroke="#d6117a" stroke-width="1.6"/></svg>Addiction</li>
        <li><svg width="10" height="8" viewBox="0 0 10 8"><path d="M1 1l3 3-3 3M5 1l3 3-3 3" fill="none" stroke="#d6117a" stroke-width="1.6"/></svg>Bullying</li>
        <li><svg width="10" height="8" viewBox="0 0 10 8"><path d="M1 1l3 3-3 3M5 1l3 3-3 3" fill="none" stroke="#d6117a" stroke-width="1.6"/></svg>Depression</li>
        <li><svg width="10" height="8" viewBox="0 0 10 8"><path d="M1 1l3 3-3 3M5 1l3 3-3 3" fill="none" stroke="#d6117a" stroke-width="1.6"/></svg>Fear</li>
        <li><svg width="10" height="8" viewBox="0 0 10 8"><path d="M1 1l3 3-3 3M5 1l3 3-3 3" fill="none" stroke="#d6117a" stroke-width="1.6"/></svg>HIV</li>
        <li><svg width="10" height="8" viewBox="0 0 10 8"><path d="M1 1l3 3-3 3M5 1l3 3-3 3" fill="none" stroke="#d6117a" stroke-width="1.6"/></svg>Loss of meaning</li>
        <li><svg width="10" height="8" viewBox="0 0 10 8"><path d="M1 1l3 3-3 3M5 1l3 3-3 3" fill="none" stroke="#d6117a" stroke-width="1.6"/></svg>Problems with Motivation/Focus</li>
        <li><svg width="10" height="8" viewBox="0 0 10 8"><path d="M1 1l3 3-3 3M5 1l3 3-3 3" fill="none" stroke="#d6117a" stroke-width="1.6"/></svg>Self sabotage</li>
        <li><svg width="10" height="8" viewBox="0 0 10 8"><path d="M1 1l3 3-3 3M5 1l3 3-3 3" fill="none" stroke="#d6117a" stroke-width="1.6"/></svg>Stress</li>
      </ul>
      <ul class="help-list col-b">
        <li><svg width="10" height="8" viewBox="0 0 10 8"><path d="M1 1l3 3-3 3M5 1l3 3-3 3" fill="none" stroke="#d6117a" stroke-width="1.6"/></svg>Anger</li>
        <li><svg width="10" height="8" viewBox="0 0 10 8"><path d="M1 1l3 3-3 3M5 1l3 3-3 3" fill="none" stroke="#d6117a" stroke-width="1.6"/></svg>Career Changes</li>
        <li><svg width="10" height="8" viewBox="0 0 10 8"><path d="M1 1l3 3-3 3M5 1l3 3-3 3" fill="none" stroke="#d6117a" stroke-width="1.6"/></svg>Difficulty making decisions</li>
        <li><svg width="10" height="8" viewBox="0 0 10 8"><path d="M1 1l3 3-3 3M5 1l3 3-3 3" fill="none" stroke="#d6117a" stroke-width="1.6"/></svg>Feeling alone/isolated</li>
        <li><svg width="10" height="8" viewBox="0 0 10 8"><path d="M1 1l3 3-3 3M5 1l3 3-3 3" fill="none" stroke="#d6117a" stroke-width="1.6"/></svg>Identity Issues</li>
        <li><svg width="10" height="8" viewBox="0 0 10 8"><path d="M1 1l3 3-3 3M5 1l3 3-3 3" fill="none" stroke="#d6117a" stroke-width="1.6"/></svg>LGBT issues</li>
        <li><svg width="10" height="8" viewBox="0 0 10 8"><path d="M1 1l3 3-3 3M5 1l3 3-3 3" fill="none" stroke="#d6117a" stroke-width="1.6"/></svg>Psychosis</li>
        <li><svg width="10" height="8" viewBox="0 0 10 8"><path d="M1 1l3 3-3 3M5 1l3 3-3 3" fill="none" stroke="#d6117a" stroke-width="1.6"/></svg>Sexual abuse</li>
        <li><svg width="10" height="8" viewBox="0 0 10 8"><path d="M1 1l3 3-3 3M5 1l3 3-3 3" fill="none" stroke="#d6117a" stroke-width="1.6"/></svg>Substance misuse</li>
      </ul>
      <ul class="help-list col-c">
        <li><svg width="10" height="8" viewBox="0 0 10 8"><path d="M1 1l3 3-3 3M5 1l3 3-3 3" fill="none" stroke="#d6117a" stroke-width="1.6"/></svg>Anxiety</li>
        <li><svg width="10" height="8" viewBox="0 0 10 8"><path d="M1 1l3 3-3 3M5 1l3 3-3 3" fill="none" stroke="#d6117a" stroke-width="1.6"/></svg>Crisis/Breakdown</li>
        <li><svg width="10" height="8" viewBox="0 0 10 8"><path d="M1 1l3 3-3 3M5 1l3 3-3 3" fill="none" stroke="#d6117a" stroke-width="1.6"/></svg>Emotional abuse</li>
        <li><svg width="10" height="8" viewBox="0 0 10 8"><path d="M1 1l3 3-3 3M5 1l3 3-3 3" fill="none" stroke="#d6117a" stroke-width="1.6"/></svg>Health Issues</li>
        <li><svg width="10" height="8" viewBox="0 0 10 8"><path d="M1 1l3 3-3 3M5 1l3 3-3 3" fill="none" stroke="#d6117a" stroke-width="1.6"/></svg>Low self confidence</li>
        <li><svg width="10" height="8" viewBox="0 0 10 8"><path d="M1 1l3 3-3 3M5 1l3 3-3 3" fill="none" stroke="#d6117a" stroke-width="1.6"/></svg>Negative thinking</li>
        <li><svg width="10" height="8" viewBox="0 0 10 8"><path d="M1 1l3 3-3 3M5 1l3 3-3 3" fill="none" stroke="#d6117a" stroke-width="1.6"/></svg>Relationship problems</li>
        <li><svg width="10" height="8" viewBox="0 0 10 8"><path d="M1 1l3 3-3 3M5 1l3 3-3 3" fill="none" stroke="#d6117a" stroke-width="1.6"/></svg>Sexuality</li>
      </ul>
    </section>
  </main>

  <footer class="site-footer">
    <nav class="footer-nav">
      <a href="#">About Me</a>
      <a href="#">Therapy</a>
      <a href="#">Common Questions</a>
      <a href="#">Blog</a>
      <a href="#">Contact Me</a>
    </nav>
    <p class="copyright">Copyright © 2021. Company Name. All Right Reserved</p>
    <div class="social">
      <span aria-label="Social link 1"></span>
      <span aria-label="Social link 2"></span>
      <span aria-label="Social link 3"></span>
      <span aria-label="Social link 4"></span>
      <span aria-label="Social link 5"></span>
    </div>
  </footer>
</body>
</html>
```